Brimvale Foods Packing Ace the Day

5 Principals for all the team to follow by!

Please can you convert the Ace the day "screenshot 2024-09-08" image into something that has a similair look and feel to the Vision and Values style?

```html
<!DOCTYPE html>
<html lang="en">
<head>
<meta charset="utf-8">
<title>Brimvale Foods Packing – Ace the Day</title>
<link rel="stylesheet" href="https://fonts.googleapis.com/css2?family=Anton&display=swap">
<style>
  :root {
    --backdrop: #c9c9c9;
    --paper: #ffffff;
    --brand-green: #6abf4b;
    --brand-red: #e01f1f;
    --ink: #161616;
    --tile-text: #ffffff;
    --icon-tint: rgba(255, 255, 255, 0.16);
    --icon-line: rgba(255, 255, 255, 0.35);
  }
  * { margin: 0; padding: 0; box-sizing: border-box; }
  html, body {
    width: 1020px;
    height: 1200px;
    overflow: hidden;
    background: var(--backdrop);
    font-family: "Anton", "Arial Narrow", sans-serif;
  }
  .principles-board {
    position: absolute;
    left: 30px;
    top: 280px;
    width: 960px;
    height: 641px;
    background: var(--paper);
    box-shadow: 0 6px 18px rgba(0, 0, 0, 0.18);
  }
  .board-header {
    position: absolute;
    left: 0; top: 0;
    width: 960px; height: 256px;
    text-align: center;
  }
  .company-name {
    position: absolute;
    left: 0; right: 0; top: 42px;
    font-size: 64px;
    line-height: 1;
    letter-spacing: 1px;
    color: var(--brand-red);
    text-transform: uppercase;
  }
  .company-rule {
    position: absolute;
    left: 179px; top: 137px;
    width: 602px; height: 3px;
    background: var(--brand-red);
  }
  .board-title {
    position: absolute;
    left: 0; right: 0; top: 170px;
    font-size: 54px;
    line-height: 1;
    color: var(--ink);
    text-transform: uppercase;
    letter-spacing: 0.5px;
  }
  .principle-tile {
    position: absolute;
    display: flex;
    align-items: center;
    justify-content: center;
    text-align: center;
    color: var(--tile-text);
    overflow: hidden;
  }
  .principle-tile.is-green { background: var(--brand-green); }
  .principle-tile.is-red { background: var(--brand-red); }
  .tile-icon {
    position: absolute;
    border: 2px solid var(--icon-line);
    background: var(--icon-tint);
    border-radius: 14px;
  }
  .tile-label {
    position: relative;
    font-size: 36px;
    line-height: 1.15;
    text-shadow: 0 1px 2px rgba(0, 0, 0, 0.15);
  }
  .tile-label small {
    display: block;
    font-size: 22px;
    line-height: 1.2;
  }
  .tile-safety   { left: 0;     top: 256px; width: 321px; height: 195px; }
  .tile-quality  { left: 324px; top: 256px; width: 320px; height: 195px; }
  .tile-team     { left: 647px; top: 256px; width: 313px; height: 195px; }
  .tile-plan     { left: 0;     top: 457px; width: 479px; height: 184px; }
  .tile-process  { left: 482px; top: 457px; width: 478px; height: 184px; }
</style>
</head>
<body>
  <main class="principles-board">
    <header class="board-header">
      <div class="company-name">Brimvale Foods Packing</div>
      <div class="company-rule"></div>
      <h1 class="board-title">The Brimvale Way.. Ace the Day</h1>
    </header>

    <section class="principle-tile is-green tile-safety">
      <div class="tile-icon" role="img" aria-label="Faint outline illustration of a worker in a hard hat with a safety shield" style="left:92px;top:16px;width:130px;height:160px;"></div>
      <p class="tile-label">H&amp;S -<br>Call It Out</p>
    </section>

    <section class="principle-tile is-red tile-quality">
      <div class="tile-icon" role="img" aria-label="Faint outline illustration of a hand holding a quality badge with a tick" style="left:100px;top:12px;width:120px;height:170px;"></div>
      <p class="tile-label">GMP / Quality -<br>Drive the Standard</p>
    </section>

    <section class="principle-tile is-green tile-team">
      <div class="tile-icon" role="img" aria-label="Faint outline sign reading behaviour" style="left:36px;top:54px;width:248px;height:92px;border-radius:2px;"></div>
      <p class="tile-label">Team &amp;<br>Behaviors -<small>What's Expected of<br>You and Your Team?</small></p>
    </section>

    <section class="principle-tile is-red tile-plan">
      <div class="tile-icon" role="img" aria-label="Faint outline illustration of a dashboard screen with a bar chart" style="left:169px;top:22px;width:150px;height:140px;"></div>
      <p class="tile-label">Plan Attainment</p>
    </section>

    <section class="principle-tile is-red tile-process">
      <div class="tile-icon" role="img" aria-label="Faint outline illustration of a plan, do, check, act cycle of arrows" style="left:168px;top:16px;width:150px;height:150px;border-radius:50%;"></div>
      <p class="tile-label">Process Control</p>
    </section>
  </main>
</body>
</html>
```